App Company Business Card Design Project

We are looking for a two sided business card design with one side in English and one side in Chinese. Information should include:
1. Name
2. Email
3. Cell phone
4. Address
Please incorporate the logo attached. Above are the only requirements.

Industry/Entity Type

Business

```html
<!DOCTYPE html>
<html lang="en">
<head>
<meta charset="utf-8">
<title>Kestrel Ridge – Business Card</title>
<link rel="stylesheet" href="https://fonts.googleapis.com/css2?family=Questrial&family=Open+Sans:wght@400&family=Lato:wght@400&family=Noto+Sans+SC:wght@400&display=swap">
<style>
  :root {
    --page: #f3f3f3;
    --page-edge: #d6d4d0;
    --card-white: #ffffff;
    --card-black: #000000;
    --brand-grey: #505052;
    --brand-grey-dark: #5a5a5c;
    --accent: #1bb5c4;
    --divider: #6a6a6a;
    --ghost: #141414;
    --shadow: rgba(0,0,0,0.45);
  }
  * { box-sizing: border-box; margin: 0; padding: 0; }
  html, body { width: 992px; height: 1200px; overflow: hidden; }
  body {
    position: relative;
    background: var(--page);
    border-top: 4px solid var(--page-edge);
    font-family: "Open Sans", sans-serif;
  }
  .card {
    position: absolute;
    left: 68px;
    width: 869px;
    height: 495px;
    box-shadow: 8px 9px 8px var(--shadow);
    overflow: hidden;
  }
  .card--front { top: 63px; background: var(--card-white); border: 1px solid #bbb; }
  .card--back { top: 622px; background: var(--card-black); }

  .brand {
    position: absolute;
    display: flex;
    align-items: center;
    gap: 22px;
    font-family: "Questrial", sans-serif;
    letter-spacing: 1px;
    white-space: nowrap;
  }
  .brand__mark { width: 30px; height: 30px; background: var(--accent); flex: none; }
  .brand--front { left: 150px; top: 106px; font-size: 50px; color: var(--brand-grey); }
  .brand--back {
    left: 80px; top: 360px;
    font-family: "Noto Sans SC", sans-serif;
    font-size: 48px; letter-spacing: 8px;
    color: var(--brand-grey-dark);
  }

  .address {
    position: absolute;
    top: 238px;
    width: 100%;
    text-align: center;
    font-family: "Lato", sans-serif;
    font-size: 23px;
    font-variant: small-caps;
    letter-spacing: 0.5px;
    color: #3c3c3c;
  }
  .contact-band {
    position: absolute;
    left: 0; top: 288px;
    width: 100%; height: 207px;
    background: var(--card-black);
  }
  .person { position: absolute; left: 67px; top: 50px; color: var(--accent); }
  .person__name { font-size: 32px; letter-spacing: 2.5px; line-height: 1; }
  .person__role { font-size: 18px; letter-spacing: 2px; margin-top: 4px; }
  .contact-band__divider {
    position: absolute; left: 423px; top: 17px;
    width: 2px; height: 134px; background: var(--divider);
  }
  .contact-list { position: absolute; left: 460px; top: 44px; list-style: none; color: var(--accent); font-size: 21px; }
  .contact-list li { display: flex; align-items: center; gap: 22px; height: 40px; }
  .contact-list svg { width: 22px; height: 24px; flex: none; }

  .ghost-shape {
    position: absolute; left: 590px; top: 75px;
    width: 190px; height: 190px;
    border: 14px solid var(--ghost);
  }
</style>
</head>
<body>
  <section class="card card--front">
    <div class="brand brand--front"><span class="brand__mark"></span>KESTREL RIDGE</div>
    <p class="address">Your address &amp; your city name USA</p>
    <div class="contact-band">
      <div class="person">
        <p class="person__name">DANIEL MOREAU</p>
        <p class="person__role">Manager</p>
      </div>
      <span class="contact-band__divider"></span>
      <ul class="contact-list">
        <li>
          <svg viewBox="0 0 22 24" aria-hidden="true"><rect x="1" y="6" width="20" height="13" fill="var(--accent)"/><path d="M1 6 L11 14 L21 6 M1 19 L8 12 M21 19 L14 12" stroke="#000" stroke-width="1.6" fill="none"/></svg>
          contact@kestrelridge.co
        </li>
        <li>
          <svg viewBox="0 0 22 24" aria-hidden="true"><rect x="3" y="1" width="16" height="22" rx="2" fill="none" stroke="var(--accent)" stroke-width="2"/><rect x="6" y="4" width="10" height="14" fill="var(--accent)"/><circle cx="11" cy="20.5" r="1" fill="var(--accent)"/></svg>
          00-481-270-936
        </li>
      </ul>
    </div>
  </section>

  <section class="card card--back" lang="zh-Hans">
    <span class="ghost-shape" aria-hidden="true"></span>
    <div class="brand brand--back"><span class="brand__mark"></span>红隼岭</div>
  </section>
</body>
</html>
```